Marta Business Card

My wife is going to start her own business with renting holiday appartments to tourists. She needs a design for a new business card... and a new web site.
Look at Stayvolt "Erholung auf dem Lindenwäldchen"

Target Market(s)

Give business card to prospects at any situation

Contact Information for Business Card

not sure what this means

Font styles to use
Script

Colors
fec41a
fee18a

Requirements
Must have
• My wife's handwriting is difficult to read:
Entspannen - Loslassen - Auftanken
Marta & das Lindenwäldchen
Urlaub an einem besonderen Ort
Marta Brecke
Grauer Pfad 7
18471 Alt Feldow
post@marta-brecke.de
www.lindenwaeldchen.net
Nice to have
• Beige background
Font like handwriting

```html
<!DOCTYPE html>
<html lang="de">
<head>
<meta charset="utf-8">
<title>Marta &amp; das Lindenwäldchen – Visitenkarte</title>
<link rel="stylesheet" href="https://fonts.googleapis.com/css2?family=Mrs+Saint+Delafield&display=swap">
<style>
  :root {
    --stage: radial-gradient(ellipse at center, #ececec 0%, #d4d4d4 100%);
    --beige: #faebd7;
    --white: #ffffff;
    --sun: #fec41a;
    --ink: #8c8c8e;
    --script: "Mrs Saint Delafield", cursive;
  }
  * { margin: 0; padding: 0; box-sizing: border-box; }
  html, body { width: 1200px; height: 446px; overflow: hidden; }
  body { background: var(--stage); position: relative; font-family: var(--script); }

  .card {
    position: absolute;
    top: 85px;
    width: 483px;
    height: 275px;
    overflow: hidden;
  }
  .card--front { left: 75px; background: var(--beige); }
  .card--back { left: 643px; background: var(--white); }

  .front-title {
    position: absolute;
    left: 0; right: 0;
    top: 98px;
    text-align: center;
    color: var(--sun);
    font-size: 50px;
    font-weight: 400;
    line-height: 1;
    white-space: nowrap;
  }
  .front-tagline {
    position: absolute;
    left: 0; right: 0;
    top: 148px;
    text-align: center;
    color: var(--ink);
    font-size: 26px;
    line-height: 1;
    white-space: nowrap;
  }

  .back-band {
    position: absolute;
    left: 0; top: 0;
    width: 100%;
    height: 138px;
    background: var(--beige);
  }
  .back-slogan {
    position: absolute;
    left: 0; right: 0;
    top: 50px;
    text-align: center;
    color: var(--ink);
    font-size: 36px;
    line-height: 1;
    white-space: nowrap;
  }
  .contact {
    position: absolute;
    color: var(--sun);
    font-size: 21px;
    line-height: 27px;
    font-style: normal;
    white-space: nowrap;
  }
  .contact--address { left: 49px; top: 165px; }
  .contact--online { left: 275px; top: 192px; }
</style>
</head>
<body>
  <section class="card card--front" aria-label="Vorderseite">
    <h1 class="front-title">Marta &amp; das Lindenwäldchen</h1>
    <p class="front-tagline">Entspannen - Loslassen - Auftanken</p>
  </section>

  <section class="card card--back" aria-label="Rückseite">
    <div class="back-band">
      <p class="back-slogan">Urlaub an einem besonderen Ort</p>
    </div>
    <address class="contact contact--address">
      Marta Brecke<br>
      Grauer Pfad 7<br>
      18471 Alt Feldow
    </address>
    <address class="contact contact--online">
      post@marta-brecke.de<br>
      www.lindenwaeldchen.net
    </address>
  </section>
</body>
</html>
```